Creative & Professional Business Card for hair salon

We are looking to update our business cards. Our salon is creative, modern, progressive and professional and looking for a design that will reflect this.

```html
<!DOCTYPE html>
<html lang="en">
<head>
<meta charset="utf-8">
<title>Velvet Strand Studio – Business Cards</title>
<link href="https://fonts.googleapis.com/css2?family=Lato:wght@300;400&display=swap" rel="stylesheet">
<style>
  :root {
    --stage: #2b2b2b;
    --card-light: #ffffff;
    --card-dark: #050505;
    --teal: #6aa6b8;
    --teal-line: #5b97aa;
    --ink: #3a3a3a;
    --rule-grey: #b9b9b9;
    --white: #f2f2f2;
  }
  * { box-sizing: border-box; margin: 0; padding: 0; }
  html, body { width: 1200px; height: 780px; overflow: hidden; }
  body {
    background: var(--stage);
    font-family: "Lato", sans-serif;
    position: relative;
  }
  .card {
    position: absolute;
    width: 540px;
    height: 309px;
    top: 236px;
    box-shadow: 0 10px 28px rgba(0,0,0,.45);
  }
  .card--appointment { left: 50px; background: var(--card-light); color: var(--ink); }
  .card--contact { left: 610px; background: var(--card-dark); color: var(--white); }

  .brand-name {
    position: absolute;
    left: 0; right: 0;
    text-align: center;
    font-weight: 300;
    color: var(--teal);
    letter-spacing: .5px;
    white-space: nowrap;
  }
  .card--appointment .brand-name { top: 48px; font-size: 26px; }

  .appointment-title {
    position: absolute;
    top: 118px; left: 36px; right: 36px;
    display: flex; align-items: center; gap: 12px;
    color: var(--teal); font-size: 14px; font-weight: 400; white-space: nowrap;
  }
  .appointment-title::before, .appointment-title::after {
    content: ""; flex: 1; height: 1px; background: var(--teal-line);
  }
  .appointment-rows { position: absolute; top: 160px; left: 36px; right: 36px; }
  .appointment-row {
    display: flex; align-items: flex-end; gap: 4px;
    font-size: 13px; height: 34px; white-space: nowrap;
  }
  .appointment-row > * { flex-shrink: 0; }
  .field-label { white-space: nowrap; }
  .field-line { height: 1px; background: var(--rule-grey); margin-bottom: 3px; }
  .field-line--name { width: 96px; margin-right: 12px; }
  .field-line--date { width: 50px; margin-right: 12px; }
  .field-line--time { width: 44px; margin-right: 10px; }
  .tick-box {
    display: inline-block; width: 10px; height: 10px;
    border: 1px solid var(--teal); margin: 0 2px 2px 4px;
  }

  .card--contact .brand-name { top: 62px; left: 120px; right: 0; font-size: 28px; }
  .contact-rule {
    position: absolute; top: 150px; left: 30px; right: 40px;
    height: 1px; background: var(--teal-line);
  }
  .person { position: absolute; left: 30px; top: 200px; white-space: nowrap; }
  .person-name { color: var(--teal); font-size: 22px; font-weight: 400; }
  .person-role { font-size: 14px; margin-top: 2px; }
  .person-address { font-size: 14px; margin-top: 22px; }
  .contact-list {
    position: absolute; right: 22px; top: 176px;
    list-style: none; text-align: right; font-size: 13px; line-height: 19px;
    white-space: nowrap;
  }
  .contact-list li { display: flex; justify-content: flex-end; align-items: center; gap: 8px; }
  .contact-list svg { width: 10px; height: 10px; flex: none; }
</style>
</head>
<body>

<section class="card card--appointment">
  <p class="brand-name">Velvet Strand Studio</p>
  <h2 class="appointment-title">Your Next Appointment</h2>
  <div class="appointment-rows">
    <div class="appointment-row"><span class="field-label">Name :</span><span class="field-line field-line--name"></span><span class="field-label">Date :</span><span class="field-line field-line--date"></span><span class="field-label">Time :</span><span class="field-line field-line--time"></span><span class="tick-box"></span><span class="field-label">AM</span><span class="tick-box"></span><span class="field-label">PM</span></div>
    <div class="appointment-row"><span class="field-label">Name :</span><span class="field-line field-line--name"></span><span class="field-label">Date :</span><span class="field-line field-line--date"></span><span class="field-label">Time :</span><span class="field-line field-line--time"></span><span class="tick-box"></span><span class="field-label">AM</span><span class="tick-box"></span><span class="field-label">PM</span></div>
    <div class="appointment-row"><span class="field-label">Name :</span><span class="field-line field-line--name"></span><span class="field-label">Date :</span><span class="field-line field-line--date"></span><span class="field-label">Time :</span><span class="field-line field-line--time"></span><span class="tick-box"></span><span class="field-label">AM</span><span class="tick-box"></span><span class="field-label">PM</span></div>
  </div>
</section>

<section class="card card--contact">
  <p class="brand-name">Velvet Strand Studio</p>
  <div class="contact-rule"></div>
  <div class="person">
    <p class="person-name">Jo Marlow</p>
    <p class="person-role">Founder</p>
    <p class="person-address">5/12 Harbour Lane, Seaview</p>
  </div>
  <ul class="contact-list">
    <li>07 5550 1234
      <svg viewBox="0 0 10 10"><path d="M2 1 L4 3 L3 4 Q4.5 6 6 7 L7 6 L9 8 L7.5 9.5 Q2 7 0.5 2.5 Z" fill="var(--teal)"/></svg></li>
    <li>salon@velvetstrand.com.au
      <svg viewBox="0 0 10 10"><rect x="0.5" y="2" width="9" height="6" fill="none" stroke="var(--teal)"/><path d="M0.5 2 L5 5.5 L9.5 2" fill="none" stroke="var(--teal)"/></svg></li>
    <li>www.velvetstrand.com.au
      <svg viewBox="0 0 10 10"><circle cx="5" cy="5" r="4.3" fill="none" stroke="var(--teal)"/><ellipse cx="5" cy="5" rx="2" ry="4.3" fill="none" stroke="var(--teal)"/><path d="M0.7 5 H9.3" stroke="var(--teal)"/></svg></li>
    <li>VelvetStrandByJoMarlow
      <svg viewBox="0 0 10 10"><circle cx="5" cy="5" r="4.5" fill="var(--teal)"/></svg></li>
  </ul>
</section>

</body>
</html>
```